Profesional personal website needs design and business card

I need a business card with my professional name as a logo "Marlo Vitality" for my business. I am a Wellness Coach, consultant and trainer. So it should be professional, wellness oriented and modern.

Target Market(s)

Private clients, governments, corporations. Luxury and high market.

Industry/Entity Type

Health And Wellness

Contact Information for Business Card

Marlo Vitality should be the logo

Colors

Designer to choose colors to be used in the design.

Requirements
Must have
• Marlo Vitality
• Name: Tomás Arribal
• Wellness Coach, Consultant & Trainer.
• Website: www.marlovitality.example
• Phone:
• Spain (+34) 612 480 397
• (USA) +1 (555) 318 2046
Nice to have
• The most important is the design of "Marlo Vitality", as this is going to be my personal brand logo. It should be professional, wellness, high end and actual.
Should not have
• no golds, no baroque style..

```html
<!DOCTYPE html>
<html lang="en">
<head>
<meta charset="utf-8">
<title>Marlo Vitality — Business Card</title>
<link rel="stylesheet" href="https://fonts.googleapis.com/css2?family=Hind:wght@700&family=PT+Sans:wght@400&display=swap">
<style>
  :root {
    --orange-light: #F99A03;
    --orange-deep: #FF7F00;
    --shadow-grey: #808080;
    --paper: #FFFFFF;
    --ink: #111111;
    --heading-font: "Hind", Arial, sans-serif;
    --body-font: "PT Sans", Arial, sans-serif;
  }
  * { margin: 0; padding: 0; box-sizing: border-box; }
  html, body { width: 1200px; height: 1000px; overflow: hidden; background: var(--paper); }
  .canvas { position: relative; width: 1200px; height: 1000px; }

  .card-shadow { position: absolute; width: 543px; height: 354px; background: var(--shadow-grey); }
  .card { position: absolute; width: 543px; height: 354px; overflow: hidden; }

  .card--front { left: 333px; top: 67px; background: var(--orange-light); }
  .card-shadow--front { left: 354px; top: 88px; }
  .front-accent {
    position: absolute; inset: 0;
    background: linear-gradient(125deg,
      rgba(255,127,0,0) 45%,
      rgba(255,127,0,0.85) 62%,
      rgba(255,127,0,0) 80%);
  }

  .brand-name {
    position: absolute; left: 104px; top: 218px;
    font-family: var(--heading-font); font-weight: 700;
    font-size: 58px; line-height: 1; color: var(--paper); white-space: nowrap;
  }

  .card--back { left: 320px; top: 519px; background: var(--paper); border: 1px solid var(--ink); }
  .card-shadow--back { left: 342px; top: 542px; }
  .back-accent {
    position: absolute; right: 0; top: 0; width: 205px; height: 240px;
    background: radial-gradient(ellipse at 100% 0%,
      var(--orange-deep) 0%,
      var(--orange-light) 55%,
      rgba(249,154,3,0) 100%);
  }

  .holder-name, .role, .contact-label {
    position: absolute; font-family: var(--heading-font); font-weight: 700; color: var(--orange-deep);
  }
  .holder-name { left: 34px; top: 34px; font-size: 31px; line-height: 1; }
  .role { left: 56px; top: 157px; font-size: 20px; line-height: 26px; }
  .contact-row { position: absolute; left: 56px; }
  .contact-row--web { top: 216px; }
  .contact-row--phone { top: 252px; }
  .contact-label { position: static; display: inline-block; width: 92px; font-size: 20px; line-height: 24px; vertical-align: top; }
  .contact-value { display: inline-block; font-family: var(--body-font); font-size: 18px; line-height: 24px; color: var(--ink); vertical-align: top; }

  .swatch { position: absolute; left: 967px; width: 62px; height: 62px; }
  .swatch--deep { top: 519px; background: var(--orange-deep); }
  .swatch--light { top: 606px; background: var(--orange-light); }
</style>
</head>
<body>
<main class="canvas">
  <div class="card-shadow card-shadow--front"></div>
  <section class="card card--front" aria-label="Card front">
    <div class="front-accent" role="img" aria-label="Decorative flowing orange band"></div>
    <div class="brand-name">Marlo Vitality</div>
  </section>

  <div class="card-shadow card-shadow--back"></div>
  <section class="card card--back" aria-label="Card back">
    <div class="back-accent" role="img" aria-label="Decorative orange corner accent"></div>
    <h1 class="holder-name">Tomás Arribal</h1>
    <p class="role">WELLNESS COACH,<br>CONSULTANT &amp; TRAINER</p>
    <div class="contact-row contact-row--web">
      <span class="contact-label">Website</span><span class="contact-value">www.marlovitality.example</span>
    </div>
    <div class="contact-row contact-row--phone">
      <span class="contact-label">Phone</span><span class="contact-value">Spain (+34) 612 480 397<br>(USA) +1 (555) 318 2046</span>
    </div>
  </section>

  <div class="swatch swatch--deep" aria-label="Deep orange colour swatch"></div>
  <div class="swatch swatch--light" aria-label="Light orange colour swatch"></div>
</main>
</body>
</html>
```